Carton Box Packaging For Motorcycle Electric Regulator - Verosta Brand

Packaging Dimensions: 7cm (H) x 6cm (W) x 2.5cm (D)
We would like to design a genuine Carton box Packaging for motorcycle electric regulator.
This is a sensitive part of the motorcycle, so we need the packaging to reflect elegant impression.
Verosta, is one of the leading companies for manufacturing Motorcycles, located in Egypt. Our company is offering high-quality products, the best in the local market, with very competitive prices.
We have a limited time to get this project done, So we Highly appreciate receiving your designs ASAP.
Target Market(s)
Motorcycle Parts Buyers
Font styles to use
Colors
Designer to choose colors to be used in the design.
Look and feel
Each slider illustrates characteristics of the customer's brand and the style your logo design should communicate.

```html
<!DOCTYPE html>
<html lang="en">
<head>
<meta charset="utf-8">
<title>Verosta Motorcycle Regulator – Carton Dieline</title>
<link href="https://fonts.googleapis.com/css2?family=Exo+2:ital,wght@0,800;1,900&display=swap" rel="stylesheet">
<style>
  :root {
    --paper: #ffffff;
    --rule: #1f1f24;
    --navy-deep: #0a1240;
    --navy-mid: #0f2a78;
    --glow: #5fc8ff;
    --yellow: #fddc2e;
    --red: #d7263d;
    --silver-light: #f2f2f2;
    --silver-mid: #9a9a9c;
    --silver-dark: #262626;
    --white: #ffffff;
    --metal: #4a4652;
  }
  * { box-sizing: border-box; margin: 0; padding: 0; }
  html, body {
    width: 1200px; height: 652px; overflow: hidden;
    background: var(--paper);
  }
  .dieline {
    position: absolute; left: 116px; top: 126px;
    width: 967px; height: 400px;
    display: flex;
    border: 2px solid var(--rule);
  }
  .side-panel {
    position: relative; width: 142px; height: 100%;
    background: var(--yellow);
    border-right: 2px solid var(--rule);
    overflow: hidden;
  }
  .side-panel .crest-art {
    position: absolute; left: 0; top: 0; width: 142px; height: 170px;
  }
  .side-panel .side-title {
    position: absolute; left: 48px; top: 178px; height: 150px;
    writing-mode: vertical-rl; transform: rotate(180deg);
    font-family: "Exo 2", sans-serif; font-style: italic; font-weight: 900;
    font-size: 19px; line-height: 21px; color: var(--red);
    text-align: left; letter-spacing: 0.5px;
  }
  .side-panel .side-brand {
    position: absolute; left: 44px; top: 338px;
    display: flex; align-items: center; gap: 4px;
    writing-mode: vertical-rl; transform: rotate(180deg);
    font-family: "Exo 2", sans-serif; font-weight: 800;
    font-size: 11px; color: var(--rule); letter-spacing: 1px;
  }
  .side-brand .dot {
    width: 30px; height: 30px; border-radius: 50%;
    background: var(--silver-mid);
  }
  .front-panel {
    position: relative; width: 341px; height: 100%;
    background: radial-gradient(ellipse at 50% 62%, var(--navy-mid) 0%, var(--navy-deep) 70%);
    border-right: 2px solid var(--rule);
    overflow: hidden;
  }
  .front-panel:last-child { border-right: none; }
  .front-panel .stage {
    position: absolute; left: 0; top: 220px; width: 100%; height: 178px;
    background: linear-gradient(180deg, rgba(95,200,255,0.55) 0%, rgba(30,90,200,0.45) 25%, rgba(12,40,120,0.5) 60%, rgba(10,18,64,0.9) 100%);
  }
  .front-panel .brand {
    position: absolute; left: 0; right: 0; top: 38px;
    display: flex; flex-direction: column; align-items: center; gap: 6px;
    font-family: "Exo 2", sans-serif; font-weight: 800;
    font-size: 13px; letter-spacing: 2px; color: var(--white);
  }
  .brand .dot {
    width: 54px; height: 54px; border-radius: 50%;
    background: var(--silver-mid);
  }
  .front-panel .title {
    position: absolute; left: 0; right: 0; top: 125px;
    text-align: center;
    font-family: "Exo 2", sans-serif; font-style: italic; font-weight: 900;
    font-size: 23px; line-height: 25px; color: var(--white);
    letter-spacing: 0.5px;
  }
  .front-panel .product {
    position: absolute; left: 93px; top: 192px; width: 156px; height: 138px;
    border-radius: 6px;
    background: linear-gradient(180deg, #5a5662 0%, var(--metal) 50%, #2f2c36 100%);
  }
</style>
</head>
<body>
  <main class="dieline">
    <section class="side-panel">
      <svg class="crest-art" viewBox="0 0 142 170" role="img" aria-label="Large silver brand crest decoration">
        <defs>
          <linearGradient id="silverA" x1="0" y1="0" x2="0" y2="1">
            <stop offset="0" stop-color="#8d8d8f"/>
            <stop offset="0.6" stop-color="#d9d9d9"/>
            <stop offset="1" stop-color="#f2f2f2"/>
          </linearGradient>
        </defs>
        <path d="M0 0 H142 V130 Q90 170 0 160 Z" fill="url(#silverA)"/>
        <path d="M0 160 Q90 170 142 130" fill="none" stroke="#262626" stroke-width="6"/>
      </svg>
      <div class="side-title">MOTORCYCLE<br>REGULATOR</div>
      <div class="side-brand"><span class="dot"></span>VEROSTA</div>
    </section>
    <section class="front-panel">
      <div class="stage" role="img" aria-label="Glowing blue digital grid floor"></div>
      <div class="brand"><span class="dot"></span>VEROSTA</div>
      <h1 class="title">MOTORCYCLE<br>REGULATOR</h1>
      <div class="product" role="img" aria-label="Photo of black finned motorcycle voltage regulator"></div>
    </section>
    <section class="side-panel">
      <svg class="crest-art" viewBox="0 0 142 170" role="img" aria-label="Large silver brand crest decoration">
        <defs>
          <linearGradient id="silverB" x1="0" y1="0" x2="0" y2="1">
            <stop offset="0" stop-color="#8d8d8f"/>
            <stop offset="0.6" stop-color="#d9d9d9"/>
            <stop offset="1" stop-color="#f2f2f2"/>
          </linearGradient>
        </defs>
        <path d="M0 0 H142 V130 Q90 170 0 160 Z" fill="url(#silverB)"/>
        <path d="M0 160 Q90 170 142 130" fill="none" stroke="#262626" stroke-width="6"/>
      </svg>
      <div class="side-title">MOTORCYCLE<br>REGULATOR</div>
      <div class="side-brand"><span class="dot"></span>VEROSTA</div>
    </section>
    <section class="front-panel">
      <div class="stage" role="img" aria-label="Glowing blue digital grid floor"></div>
      <div class="brand"><span class="dot"></span>VEROSTA</div>
      <h1 class="title">MOTORCYCLE<br>REGULATOR</h1>
      <div class="product" role="img" aria-label="Photo of black finned motorcycle voltage regulator"></div>
    </section>
  </main>
</body>
</html>
```